Whitby's Yard & Garden Center Business Card Update

I need an updated Business card design for my Lawn and Garden Center. We do Landscaping installs, Lawn Mowing, Snow Removal and also have a Garden Center Retail Division. I uploaded a few of our previous business cards to give an idea of what we are starting with. The main goal of this update is to simplify and modernize the business card, not all of the services that are on the previous cards has to be on the new one but I would still like to highlight our main services. There is also a sample of our logo that Can be used in the design.

Industry/Entity Type

Landscaping

Contact Information for Business Card

Desmond Whitby
Desmond@Whitbysyardandgarden.example
Business (555) 208-7316
Cell (555) 391-6842

Colors

Designer to choose colors to be used in the design.

Requirements
Must have
• Services Provided :
• Landscaping
• Lawn Maintenance
• Snow Removal
• Garden Center

```html
<!DOCTYPE html>
<html lang="en">
<head>
<meta charset="utf-8">
<title>Whitby's Yard &amp; Garden Center – Business Card</title>
<link href="https://fonts.googleapis.com/css2?family=Lato:wght@400;700&display=swap" rel="stylesheet">
<style>
  :root {
    --backdrop: #3a322d;
    --card: #0b0c0d;
    --edge: #2f5a2a;
    --green: #2f6a2a;
    --white: #ffffff;
    --muted: #d9d9d9;
    --divider: #3f7a36;
  }
  * { box-sizing: border-box; margin: 0; padding: 0; }
  html, body { width: 1200px; height: 847px; overflow: hidden; }
  body {
    background: var(--backdrop);
    font-family: "Lato", Arial, sans-serif;
    position: relative;
  }
  .card {
    position: absolute;
    width: 540px;
    height: 309px;
    background: var(--card);
    border: 1px solid var(--edge);
    box-shadow: 0 14px 30px rgba(0,0,0,.45);
  }
  .card--front { left: 50px; top: 90px; }
  .card--back  { left: 610px; top: 450px; }

  .brand {
    display: flex;
    align-items: center;
    gap: 12px;
    color: var(--white);
    font-weight: 700;
  }
  .brand__mark {
    width: 22px; height: 22px;
    background: var(--green);
  }
  .card--front .brand {
    position: absolute;
    left: 0; right: 0; top: 110px;
    justify-content: center;
    font-size: 54px;
  }
  .card--front .brand__mark { width: 34px; height: 34px; }
  .card--front .site {
    position: absolute;
    left: 0; right: 0; bottom: 44px;
    text-align: center;
    color: var(--muted);
    font-size: 14px;
    letter-spacing: 3px;
  }

  .person { position: absolute; left: 30px; top: 28px; }
  .person__name { color: var(--green); font-weight: 700; font-size: 26px; }
  .person__title { color: var(--muted); font-size: 13px; margin-top: 2px; }

  .contacts {
    position: absolute; left: 30px; top: 118px;
    list-style: none;
    color: var(--white);
    font-size: 14px;
    line-height: 22px;
  }
  .contacts li { display: flex; align-items: center; gap: 10px; }
  .contacts svg { width: 13px; height: 13px; fill: none; stroke: var(--green); stroke-width: 2; flex: none; }

  .card--back .brand {
    position: absolute; right: 34px; top: 128px;
    font-size: 40px;
  }

  .services {
    position: absolute; left: 30px; right: 30px; bottom: 26px;
    display: flex; justify-content: space-between;
    color: var(--white);
    font-size: 15px;
  }
  .services span + span::before {
    content: "|";
    color: var(--divider);
    margin-right: 12px;
  }
</style>
</head>
<body>

<section class="card card--front">
  <div class="brand"><span class="brand__mark"></span>Whitby's</div>
  <p class="site">www.Whitbysyardandgarden.example</p>
</section>

<section class="card card--back">
  <div class="person">
    <h1 class="person__name">Desmond Whitby</h1>
    <p class="person__title">Founder &amp; CEO</p>
  </div>

  <ul class="contacts">
    <li><svg viewBox="0 0 16 16"><path d="M3 2h3l1 4-2 1a9 9 0 0 0 4 4l1-2 4 1v3a1 1 0 0 1-1 1A13 13 0 0 1 2 3a1 1 0 0 1 1-1z"/></svg>(555) 208-7316</li>
    <li><svg viewBox="0 0 16 16"><rect x="4" y="1" width="8" height="14" rx="1.5"/><path d="M7 12h2"/></svg>(555) 391-6842</li>
    <li><svg viewBox="0 0 16 16"><rect x="1" y="3" width="14" height="10"/><path d="M1 3l7 6 7-6"/></svg>Desmond@Whitbysyardandgarden.example</li>
    <li><svg viewBox="0 0 16 16"><circle cx="8" cy="8" r="6.5"/><path d="M1.5 8h13M8 1.5c3 3 3 10 0 13M8 1.5c-3 3-3 10 0 13"/></svg>www.Whitbysyardandgarden.example</li>
  </ul>

  <div class="brand"><span class="brand__mark"></span>Whitby's</div>

  <p class="services">
    <span>Landscaping</span>
    <span>Lawn Maintenance</span>
    <span>Snow Removal</span>
    <span>Garden Center</span>
  </p>
</section>

</body>
</html>
```